Business Card Design

I'm a commercial general contractor remodel offices, hotels, health clubs and stores mostly San Francisco and the peninsula
the file I down loaded is kind of what I want I like the I beam with my company name in it, that would be fine with me but if you have better Idea will look at it you never know, I'm decided to give in and change my company name to how every one knows me, I have been in business since 1991, I like the I beam logo I included one of my old card from my old company for reference for you.

Industry/Entity Type

Business

Contact Information for Business Card

BRAXO CONSTRUCTION (is my company name)
Wendell Trusk contractor, LIc 314827
4158 Garnet Row, San Bruno, California 94066
mobile, (415) 555-0147
phone (650) 555-0182
Fax, (650) 555-0183
email, braxo@braxoconstruction.example

```html
<!DOCTYPE html>
<html lang="en">
<head>
<meta charset="UTF-8">
<title>Braxo Construction — Business Card</title>
<link href="https://fonts.googleapis.com/css2?family=Source+Sans+3:wght@400;600;700&display=swap" rel="stylesheet">
<style>
  :root {
    --backdrop: #e9e7e3;
    --card: #fbfaf7;
    --brand-blue: #2a8bc4;
    --ink-navy: #2b3479;
    --icon-grey: #a3a6ab;
    --white: #ffffff;
  }
  * { margin: 0; padding: 0; box-sizing: border-box; }
  html, body {
    width: 1200px; height: 800px; overflow: hidden;
    background: var(--backdrop);
    font-family: "Source Sans 3", "Myriad Pro", sans-serif;
  }
  .card {
    position: absolute; left: 180px; top: 160px;
    width: 840px; height: 480px;
    background: var(--card);
    box-shadow: 0 6px 24px rgba(0,0,0,0.15);
    overflow: hidden;
  }
  .company-band {
    position: absolute; left: 300px; right: 0; top: 34px; height: 46px;
    background: var(--brand-blue);
    color: var(--white);
    font-weight: 700; font-size: 33px; letter-spacing: 0.5px;
    line-height: 46px; padding-left: 22px;
  }
  .brand-mark {
    position: absolute; left: 34px; top: 96px;
    display: flex; align-items: center; gap: 14px;
    color: var(--ink-navy);
    font-weight: 700; font-size: 40px;
  }
  .brand-mark .square {
    width: 26px; height: 26px; background: var(--brand-blue);
  }
  .person-name {
    position: absolute; right: 56px; top: 168px;
    color: var(--ink-navy);
    font-size: 56px; font-weight: 400; line-height: 1;
  }
  .role-band {
    position: absolute; left: 0; right: 0; top: 240px; height: 36px;
    background: var(--brand-blue);
  }
  .role-band .role {
    position: absolute; right: 56px; top: 0;
    color: var(--white); font-size: 27px; line-height: 34px;
  }
  .contact {
    position: absolute;
    color: var(--ink-navy);
    font-size: 30px; line-height: 1;
    display: flex; align-items: center; gap: 10px;
  }
  .contact svg { width: 20px; height: 20px; fill: var(--icon-grey); flex: none; }
  .contact.mobile { right: 56px; top: 294px; }
  .contact.phone  { right: 56px; top: 336px; }
  .contact.fax    { left: 190px; top: 358px; }
  .contact.email  { left: 190px; top: 400px; }
  .contact.address { left: 190px; top: 442px; font-size: 24px; }
  .contact.fax svg { width: 26px; height: 24px; }
</style>
</head>
<body>
  <main class="card">
    <div class="brand-mark"><span class="square"></span><span class="brand-name">BRAXO, INC.</span></div>
    <div class="company-band">BRAXO CONSTRUCTION</div>

    <h1 class="person-name">Wendell Trusk</h1>
    <div class="role-band"><span class="role">contractor · Lic 314827</span></div>

    <div class="contact mobile">
      <svg viewBox="0 0 24 24" aria-hidden="true"><path d="M6.6 10.8a15.1 15.1 0 0 0 6.6 6.6l2.2-2.2a1 1 0 0 1 1-.25 11.4 11.4 0 0 0 3.6.57 1 1 0 0 1 1 1V20a1 1 0 0 1-1 1A17 17 0 0 1 3 4a1 1 0 0 1 1-1h3.5a1 1 0 0 1 1 1c0 1.25.2 2.45.57 3.57a1 1 0 0 1-.25 1z"/></svg>
      <span>(415) 555-0147</span>
    </div>
    <div class="contact phone">
      <svg viewBox="0 0 24 24" aria-hidden="true"><path d="M6.6 10.8a15.1 15.1 0 0 0 6.6 6.6l2.2-2.2a1 1 0 0 1 1-.25 11.4 11.4 0 0 0 3.6.57 1 1 0 0 1 1 1V20a1 1 0 0 1-1 1A17 17 0 0 1 3 4a1 1 0 0 1 1-1h3.5a1 1 0 0 1 1 1c0 1.25.2 2.45.57 3.57a1 1 0 0 1-.25 1z"/></svg>
      <span>(650) 555-0182</span>
    </div>
    <div class="contact fax">
      <svg viewBox="0 0 26 24" aria-hidden="true"><rect x="7" y="1" width="12" height="6"/><rect x="1" y="8" width="24" height="10" rx="2"/><rect x="7" y="15" width="12" height="8" fill="#fbfaf7" stroke="#a3a6ab" stroke-width="2"/></svg>
      <span>(650) 555-0183</span>
    </div>
    <div class="contact email"><span>braxo@braxoconstruction.example</span></div>
    <div class="contact address"><span>4158 Garnet Row, San Bruno, California 94066</span></div>
  </main>
</body>
</html>
```